Business needs Office Posters Designed

I need a office poster designed to put on a 2 feet x 3 feet space:
My Employee is Better Than Me.
- to signify the importance of listening to your employees, because they know better, more experienced in their respective fields.

Target Market(s)

employees

Industry/Entity Type

Healthcare

```html
<!DOCTYPE html>
<html lang="en">
<head>
<meta charset="utf-8">
<title>My Employee Is Better Than Me</title>
<link rel="stylesheet" href="https://fonts.googleapis.com/css2?family=Archivo:wdth,wght@62..125,900&family=Montserrat:wght@200&display=swap">
<style>
  :root {
    --navy: #14185a;
    --deep: #1b0a24;
    --gold: #e7a924;
    --amber: #f0b030;
    --green: #2f6b3e;
    --teal: #1d4c48;
    --crimson: #c5203e;
    --rose: #d8305a;
    --white: #ffffff;
    --violet: #4a3ff0;
    --yellow: #e8ad22;
    --ghost: rgba(255, 255, 255, 0.32);
  }
  * { margin: 0; padding: 0; box-sizing: border-box; }
  html, body { width: 800px; height: 1200px; overflow: hidden; background: var(--deep); }
  .poster {
    position: relative;
    width: 800px;
    height: 1200px;
    overflow: hidden;
  }
  .bokeh-backdrop {
    position: absolute;
    inset: 0;
    background:
      radial-gradient(circle at 50% 48%, var(--teal) 0%, var(--green) 14%, rgba(47,107,62,0) 30%),
      radial-gradient(ellipse 62% 38% at 50% 36%, rgba(240,176,48,0.95) 0%, rgba(231,169,36,0.7) 45%, rgba(231,169,36,0) 80%),
      radial-gradient(ellipse 70% 34% at 45% 72%, rgba(216,48,90,0.9) 0%, rgba(197,32,62,0.7) 45%, rgba(197,32,62,0) 85%),
      radial-gradient(ellipse 40% 30% at 85% 30%, rgba(230,120,40,0.7) 0%, rgba(230,120,40,0) 80%),
      linear-gradient(180deg, var(--navy) 0%, #2a2466 18%, #5a3a40 45%, #6a1830 75%, var(--deep) 100%);
    filter: blur(8px);
    transform: scale(1.05);
  }
  .ghost-words {
    position: absolute;
    inset: 0;
    font-family: "Montserrat", sans-serif;
    font-weight: 200;
    color: var(--ghost);
    filter: blur(4px);
    white-space: nowrap;
  }
  .ghost-words span {
    position: absolute;
    left: 50%;
    transform: translateX(-50%);
    line-height: 1;
  }
  .ghost-my { top: 80px; font-size: 250px; }
  .ghost-employee { top: 390px; font-size: 230px; }
  .ghost-better { top: 660px; font-size: 230px; }
  .ghost-me { top: 900px; font-size: 250px; }
  .headline {
    position: absolute;
    left: 0;
    right: 0;
    top: 380px;
    text-align: center;
    font-family: "Archivo", sans-serif;
    font-weight: 900;
    font-stretch: 75%;
    font-size: 112px;
    line-height: 0.9;
    text-transform: uppercase;
    transform: rotate(-12deg);
    transform-origin: 50% 50%;
    text-shadow: 6px 10px 10px rgba(0, 0, 0, 0.75);
  }
  .headline .line { display: block; }
  .white { color: var(--white); }
  .violet { color: var(--violet); }
  .yellow { color: var(--yellow); }
</style>
</head>
<body>
  <main class="poster">
    <div class="bokeh-backdrop" role="img" aria-label="Blurred colourful bokeh lights in navy, gold, green and crimson tones"></div>
    <div class="ghost-words" aria-hidden="true">
      <span class="ghost-my">My</span>
      <span class="ghost-employee">employee</span>
      <span class="ghost-better">better than</span>
      <span class="ghost-me">Me</span>
    </div>
    <h1 class="headline">
      <span class="line white">My</span>
      <span class="line"><span class="white">Employee</span> <span class="violet">is</span></span>
      <span class="line violet">Better than</span>
      <span class="line yellow">Me</span>
    </h1>
  </main>
</body>
</html>
```